Slide Master for Halvern Engines - A Systematic Hedge Fund

We are looking for someone to produce a theme and slide master for us for our investor presentations. I have uploaded a few examples of templates that we would like to have included:
Main Title
Section Title
Slides with just bullet points
Different image/table configurations with bullet points and foot notes
Biographies of different lengths
A disclaimer (no one will read this but it should still look nice and needs to be in the presentations)
I have also uploaded the company logo, business card and colour definitions. Currently we have a blue colour scheme defined, but it would be nice to get a complementary set of colours so that when we have charts with more elements we can just draw from those.
The most important thing is that the slide master must be of general use to us. We arn't looking to have a specific presentation designed for us, but a theme/style that we can apply ourselves to any presentation we need to give in the future. It should have clearly defined guidelines for where content should go (and if this is different with and without footnotes for example). We would also like it to have a similar feel to the logo/business cards, so matt colours, high contrast, but not busy.
I'm excited to see the results!

```html
<!DOCTYPE html>
<html lang="en">
<head>
<meta charset="utf-8">
<title>Halvern Engines – Slide Master Layouts</title>
<link href="https://fonts.googleapis.com/css2?family=Roboto:wght@300;400;700&display=swap" rel="stylesheet">
<style>
  :root {
    --sheet: #e6e6e6;
    --slide: #ffffff;
    --navy: #0b4778;
    --title: #1b5a8c;
    --blue: #5b9bd9;
    --green: #8dcc4e;
    --bar-light: #f0f0f0;
    --bar-grey: #d9d9d9;
    --rule: #c9ccd0;
    --muted: #a6a9ad;
    --text: #333a40;
    --body: #4a5158;
    --sheet-num: #555a5f;
  }
  * { box-sizing: border-box; margin: 0; padding: 0; }
  html, body { width: 1200px; height: 724px; overflow: hidden; }
  body { background: var(--sheet); font-family: "Roboto", sans-serif; color: var(--text); position: relative; }

  .slide { position: absolute; width: 544px; height: 306px; background: var(--slide); overflow: hidden; }
  .slide--5 { left: 39px; top: 41px; }
  .slide--6 { left: 617px; top: 41px; }
  .slide--7 { left: 39px; top: 378px; }
  .slide--8 { left: 617px; top: 378px; }

  .slide__title { position: absolute; left: 29px; top: 30px; font-size: 18.5px; font-weight: 300; color: var(--title); letter-spacing: -0.2px; }
  .slide__title strong { font-weight: 700; color: var(--navy); }
  .slide__section { position: absolute; right: 30px; top: 43px; font-size: 10px; font-weight: 300; color: var(--muted); letter-spacing: 0.2px; }
  .slide__rule { position: absolute; left: 29px; right: 30px; top: 56px; height: 1px; background: var(--rule); }

  .slide__classification { position: absolute; left: 6px; bottom: 4px; font-size: 4.6px; font-weight: 700; color: var(--body); letter-spacing: 0.1px; }
  .slide__brand { position: absolute; right: 24px; bottom: 6px; font-size: 5px; font-weight: 700; color: var(--navy); display: flex; align-items: center; gap: 2px; }
  .slide__brand::before { content: ""; width: 4px; height: 4px; border-radius: 50%; background: var(--navy); }
  .slide__page { position: absolute; right: 10px; bottom: 5px; font-size: 5.5px; color: var(--text); }

  /* timeline list */
  .timeline { position: absolute; top: 92px; width: 200px; }
  .timeline--left { left: 34px; }
  .timeline--right { left: 230px; }
  .timeline::before { content: ""; position: absolute; left: 0; top: 4px; height: 88px; width: 1px; background: var(--blue); }
  .timeline__item { position: relative; padding-left: 15px; height: 44px; }
  .timeline__item::before { content: ""; position: absolute; left: -3.5px; top: 2px; width: 7px; height: 7px; border-radius: 50%; background: var(--navy); }
  .timeline__item--accent::before { background: var(--blue); }
  .timeline__heading { font-size: 8.8px; font-weight: 400; color: var(--text); line-height: 11px; }
  .timeline__text { font-size: 6.4px; font-weight: 300; color: var(--body); line-height: 8px; margin-top: 3px; width: 160px; }

  /* progress steps */
  .steps { position: absolute; left: 0; top: 0; width: 544px; height: 306px; }
  .step { position: absolute; width: 80px; text-align: center; }
  .step__value { font-size: 13.5px; font-weight: 400; color: var(--navy); line-height: 15px; }
  .step__value--light { color: var(--blue); }
  .step__text { font-size: 6.4px; font-weight: 300; color: var(--body); line-height: 8.2px; margin-top: 1px; }

  /* bullets */
  .bullets { position: absolute; list-style: none; }
  .bullets li { position: relative; padding-left: 11px; font-weight: 300; color: var(--text); }
  .bullets li::before { content: ""; position: absolute; left: 0; width: 2.4px; height: 2.4px; border-radius: 50%; background: var(--blue); }
  .bullets--small li { font-size: 8px; line-height: 12.5px; }
  .bullets--small li::before { top: 4.5px; }
  .bullets--large li { font-size: 9px; line-height: 11px; margin-bottom: 5.5px; }
  .bullets--large li::before { top: 4px; }

  .chart-title { position: absolute; font-size: 9.5px; font-weight: 400; color: var(--blue); }
  .chart { position: absolute; }
  .chart text { font-family: "Roboto", sans-serif; font-size: 5.6px; fill: #8a8e92; font-weight: 300; }

  .footnote { position: absolute; left: 0; top: 272px; width: 128px; height: 1px; background: var(--rule); }
  .footnote__text { position: absolute; left: 9px; top: 278px; width: 290px; font-size: 4.3px; line-height: 6.2px; font-weight: 300; color: #8a8e92; }

  .sheet-number { position: absolute; right: 12px; bottom: 8px; font-size: 38px; font-weight: 700; color: var(--sheet-num); line-height: 1; }
</style>
</head>
<body>

<!-- Slide 5: timeline headings -->
<section class="slide slide--5">
  <h2 class="slide__title">Sub-Heading <strong>Tittle</strong></h2>
  <span class="slide__section">SECTION TITTLE</span>
  <div class="slide__rule"></div>

  <div class="timeline timeline--left">
    <div class="timeline__item"><div class="timeline__heading">Heading A</div><div class="timeline__text">Lorem ipsum dolor sit amet, consectetura dipiscing elit dolor sit amet Lorem ipsum dolor sit</div></div>
    <div class="timeline__item timeline__item--accent"><div class="timeline__heading">Heading B</div><div class="timeline__text">Lorem ipsum dolor sit amet, consectetura dipiscing elit dolor sit amet Lorem ipsum dolor sit</div></div>
    <div class="timeline__item"><div class="timeline__heading">Heading C</div><div class="timeline__text">Lorem ipsum dolor sit amet, consectetura dipiscing elit dolor sit amet Lorem ipsum dolor sit</div></div>
  </div>
  <div class="timeline timeline--right">
    <div class="timeline__item"><div class="timeline__heading">Heading D</div><div class="timeline__text">Lorem ipsum dolor sit amet, consectetura dipiscing elit dolor sit amet Lorem ipsum dolor sit</div></div>
    <div class="timeline__item timeline__item--accent"><div class="timeline__heading">Heading E</div><div class="timeline__text">Lorem ipsum dolor sit amet, consectetura dipiscing elit dolor sit amet Lorem ipsum dolor sit</div></div>
    <div class="timeline__item"><div class="timeline__heading">Heading F</div><div class="timeline__text">Lorem ipsum dolor sit amet, consectetura dipiscing elit dolor sit amet Lorem ipsum dolor sit</div></div>
  </div>

  <span class="slide__classification">NOT FOR CIRCULATION</span>
  <span class="slide__brand">Halvern Engines</span>
  <span class="slide__page">5</span>
</section>

<!-- Slide 6: progress steps -->
<section class="slide slide--6">
  <h2 class="slide__title">Sub-Heading <strong>Tittle</strong></h2>
  <span class="slide__section">SECTION TITTLE</span>
  <div class="slide__rule"></div>

  <svg class="steps" viewBox="0 0 544 306" aria-hidden="true">
    <g stroke="#cfd8e0" stroke-width="0.6">
      <line x1="92" y1="143" x2="209" y2="152"/>
      <line x1="209" y1="152" x2="327" y2="143"/>
      <line x1="327" y1="143" x2="446" y2="152"/>
    </g>
    <g fill="none" stroke="#eeeeee" stroke-width="7">
      <path d="M 62 143 A 30 30 0 0 0 92 173"/>
      <path d="M 209 122 A 30 30 0 0 0 209 182"/>
      <path d="M 327 113 A 30 30 0 0 0 297 143"/>
      <path d="M 446 122 A 30 30 0 0 1 446 182 A 30 30 0 0 1 446 122"/>
    </g>
    <circle cx="92" cy="143" r="26" fill="var(--navy)"/>
    <circle cx="209" cy="152" r="26" fill="var(--blue)"/>
    <circle cx="327" cy="143" r="26" fill="var(--navy)"/>
    <circle cx="446" cy="152" r="26" fill="var(--blue)"/>
    <g fill="none" stroke="#fff" stroke-width="1.6" stroke-linecap="round" stroke-linejoin="round">
      <circle cx="92" cy="143" r="11"/><circle cx="92" cy="143" r="7"/><circle cx="92" cy="143" r="3"/>
      <path d="M92 143 L 105 130 M102 130 h3 v3"/>
      <path d="M199 163 h20 M201 163 v-6 M205 163 v-9 M209 163 v-5 M213 163 v-8 M217 163 v-11 M200 152 l5 -5 4 3 8 -8 M214 142 h3 v3"/>
      <circle cx="327" cy="143" r="11"/><ellipse cx="327" cy="143" rx="4.5" ry="11"/><path d="M316 143 h22 M318 137 h18 M318 149 h18"/>
      <path d="M439 159 l3 -7 c4 -9 10 -14 15 -15 c-1 5 -6 11 -15 15 M440 153 l-4 -1 4 -5 5 0 M444 156 l1 4 5 -4 0 -5 M437 162 l-3 3"/>
    </g>
  </svg>

  <div class="step" style="left:52px;top:186px"><div class="step__value">25%</div><div class="step__text">Lorem ipsum dolor sit amet, consectetura dipiscing elit</div></div>
  <div class="step" style="left:169px;top:195px"><div class="step__value step__value--light">50%</div><div class="step__text">Lorem ipsum dolor sit amet, consectetura dipiscing elit</div></div>
  <div class="step" style="left:287px;top:186px"><div class="step__value">75%</div><div class="step__text">Lorem ipsum dolor sit amet, consectetura dipiscing elit</div></div>
  <div class="step" style="left:406px;top:195px"><div class="step__value step__value--light">100%</div><div class="step__text">Lorem ipsum dolor sit amet, consectetura dipiscing elit</div></div>

  <span class="slide__classification">NOT FOR CIRCULATION</span>
  <span class="slide__brand">Halvern Engines</span>
  <span class="slide__page">6</span>
</section>

<!-- Slide 7: two bar charts with footnote -->
<section class="slide slide--7">
  <h2 class="slide__title">Sub-heading <strong>Tittle*</strong></h2>
  <span class="slide__section">SECTION TITTLE</span>
  <div class="slide__rule"></div>

  <ul class="bullets bullets--small" style="left:33px;top:80px">
    <li>Lorem ipsum dolor sit amet, consecterura</li>
    <li>Lorem ipsum dolor sit amet, consecterura</li>
  </ul>
  <ul class="bullets bullets--small" style="left:219px;top:80px">
    <li>Lorem ipsum dolor sit amet, consecterura</li>
    <li>Lorem ipsum dolor sit amet, consecterura</li>
  </ul>

  <h3 class="chart-title" style="left:28px;top:116px">Tittle of bar chart</h3>
  <h3 class="chart-title" style="left:264px;top:115px">Tittle of bar chart</h3>

  <svg class="chart" style="left:20px;top:135px" width="240" height="125" viewBox="0 0 240 125" role="img" aria-label="Bar chart, values by category 100 to 1300">
    <g text-anchor="end"><text x="16" y="9">5</text><text x="16" y="29">4</text><text x="16" y="49">3</text><text x="16" y="69">2</text><text x="16" y="89">1</text><text x="16" y="109">0</text></g>
    <rect x="25" y="87" width="15.6" height="20" fill="var(--bar-light)"/>
    <rect x="40.6" y="67" width="15.6" height="40" fill="var(--bar-grey)"/>
    <rect x="56.2" y="87" width="15.6" height="20" fill="var(--bar-grey)"/>
    <rect x="71.8" y="39" width="15.6" height="68" fill="var(--navy)"/>
    <rect x="87.4" y="47" width="15.6" height="60" fill="var(--bar-light)"/>
    <rect x="103" y="67" width="15.6" height="40" fill="var(--bar-grey)"/>
    <rect x="118.6" y="7" width="15.6" height="100" fill="var(--blue)"/>
    <rect x="134.2" y="17" width="15.6" height="90" fill="var(--bar-light)"/>
    <rect x="149.8" y="67" width="15.6" height="40" fill="var(--bar-grey)"/>
    <rect x="165.4" y="47" width="15.6" height="60" fill="var(--bar-light)"/>
    <rect x="181" y="87" width="15.6" height="20" fill="var(--green)"/>
    <rect x="196.6" y="47" width="15.6" height="60" fill="var(--bar-grey)"/>
    <rect x="212.2" y="87" width="15.6" height="20" fill="var(--bar-light)"/>
    <g text-anchor="middle"><text x="32.8" y="118">100</text><text x="48.4" y="118">200</text><text x="64" y="118">300</text><text x="79.6" y="118">400</text><text x="95.2" y="118">500</text><text x="110.8" y="118">600</text><text x="126.4" y="118">700</text><text x="142" y="118">800</text><text x="157.6" y="118">900</text><text x="173.2" y="118">1000</text><text x="188.8" y="118">1100</text><text x="204.4" y="118">1200</text><text x="220" y="118">1300</text></g>
  </svg>

  <svg class="chart" style="left:256px;top:135px" width="240" height="125" viewBox="0 0 240 125" role="img" aria-label="Bar chart, values by category 100 to 1300">
    <g text-anchor="end"><text x="16" y="9">5</text><text x="16" y="29">4</text><text x="16" y="49">3</text><text x="16" y="69">2</text><text x="16" y="89">1</text><text x="16" y="109">0</text></g>
    <rect x="25" y="87" width="15.6" height="20" fill="var(--bar-light)"/>
    <rect x="40.6" y="67" width="15.6" height="40" fill="var(--bar-grey)"/>
    <rect x="56.2" y="87" width="15.6" height="20" fill="var(--bar-grey)"/>
    <rect x="71.8" y="39" width="15.6" height="68" fill="var(--green)"/>
    <rect x="87.4" y="47" width="15.6" height="60" fill="var(--bar-light)"/>
    <rect x="103" y="67" width="15.6" height="40" fill="var(--bar-grey)"/>
    <rect x="118.6" y="7" width="15.6" height="100" fill="var(--blue)"/>
    <rect x="134.2" y="17" width="15.6" height="90" fill="var(--bar-light)"/>
    <rect x="149.8" y="67" width="15.6" height="40" fill="var(--bar-grey)"/>
    <rect x="165.4" y="47" width="15.6" height="60" fill="var(--bar-light)"/>
    <rect x="181" y="87" width="15.6" height="20" fill="var(--navy)"/>
    <rect x="196.6" y="47" width="15.6" height="60" fill="var(--bar-grey)"/>
    <rect x="212.2" y="87" width="15.6" height="20" fill="var(--bar-light)"/>
    <g text-anchor="middle"><text x="32.8" y="118">100</text><text x="48.4" y="118">200</text><text x="64" y="118">300</text><text x="79.6" y="118">400</text><text x="95.2" y="118">500</text><text x="110.8" y="118">600</text><text x="126.4" y="118">700</text><text x="142" y="118">800</text><text x="157.6" y="118">900</text><text x="173.2" y="118">1000</text><text x="188.8" y="118">1100</text><text x="204.4" y="118">1200</text><text x="220" y="118">1300</text></g>
  </svg>

  <div class="footnote"></div>
  <p class="footnote__text">* Lorem ipsum dolor sit amet, consectetur adipiscing elit. Vestibulum lacinia eros eu pharetra mollis. Nullam vulputate purus mi, sed maximus est sodales mollis. Mauris nec vulputate eros. Cras lectus lacus, lacinia eu dapibus ac, tincidunt eu nisi. Suspendisse in volutpat risus. Nunc pharetra porttitor lorem.</p>

  <span class="slide__brand">Halvern Engines</span>
  <span class="slide__page">7</span>
</section>

<!-- Slide 8: single bar chart with bullets and footnote -->
<section class="slide slide--8">
  <h2 class="slide__title">Sub-heading <strong>Tittle*</strong></h2>
  <span class="slide__section">SECTION TITTLE</span>
  <div class="slide__rule"></div>

  <h3 class="chart-title" style="left:27px;top:83px">Tittle of bar chart</h3>

  <svg class="chart" style="left:20px;top:105px" width="300" height="150" viewBox="0 0 300 150" role="img" aria-label="Bar chart, values by category 100 to 1300">
    <g text-anchor="end"><text x="16" y="9">5</text><text x="16" y="35">4</text><text x="16" y="61">3</text><text x="16" y="87">2</text><text x="16" y="113">1</text><text x="16" y="139">0</text></g>
    <rect x="24" y="111" width="20.7" height="26" fill="var(--bar-light)"/>
    <rect x="44.7" y="85" width="20.7" height="52" fill="var(--bar-grey)"/>
    <rect x="65.4" y="111" width="20.7" height="26" fill="var(--bar-light)"/>
    <rect x="86.1" y="48.6" width="20.7" height="88.4" fill="var(--blue)"/>
    <rect x="106.8" y="59" width="20.7" height="78" fill="var(--bar-light)"/>
    <rect x="127.5" y="85" width="20.7" height="52" fill="var(--bar-grey)"/>
    <rect x="148.2" y="7" width="20.7" height="130" fill="var(--navy)"/>
    <rect x="168.9" y="20" width="20.7" height="117" fill="var(--bar-light)"/>
    <rect x="189.6" y="85" width="20.7" height="52" fill="var(--bar-grey)"/>
    <rect x="210.3" y="59" width="20.7" height="78" fill="var(--bar-light)"/>
    <rect x="231" y="111" width="20.7" height="26" fill="var(--green)"/>
    <rect x="251.7" y="59" width="20.7" height="78" fill="var(--bar-grey)"/>
    <rect x="272.4" y="111" width="20.7" height="26" fill="var(--bar-light)"/>
    <g text-anchor="middle"><text x="34.3" y="148">100</text><text x="55" y="148">200</text><text x="75.7" y="148">300</text><text x="96.4" y="148">400</text><text x="117.1" y="148">500</text><text x="137.8" y="148">600</text><text x="158.5" y="148">700</text><text x="179.2" y="148">800</text><text x="199.9" y="148">900</text><text x="220.6" y="148">1000</text><text x="241.3" y="148">1100</text><text x="262" y="148">1200</text><text x="282.7" y="148">1300</text></g>
  </svg>

  <ul class="bullets bullets--large" style="left:335px;top:119px;width:110px">
    <li>Lorem ipsum dolor sit amet, consectetura dipiscing elit</li>
    <li>Lorem ipsum dolor sit amet, consectetura dipiscing elit</li>
    <li>Lorem ipsum dolor sit amet, consectetura dipiscing elit</li>
  </ul>

  <div class="footnote"></div>
  <p class="footnote__text">* Lorem ipsum dolor sit amet, consectetur adipiscing elit. Vestibulum lacinia eros eu pharetra mollis. Nullam vulputate purus mi, sed maximus est sodales mollis. Mauris nec vulputate eros. Cras lectus lacus, lacinia eu dapibus ac, tincidunt eu nisi. Suspendisse in volutpat risus. Nunc pharetra porttitor lorem.</p>

  <span class="slide__brand">Halvern Engines</span>
  <span class="slide__page">8</span>
</section>

<span class="sheet-number">2</span>

</body>
</html>
```